Business Card for my building company

I would like the card to make a statement, so as soon as you see the card you think "wow nice card' and then read the details on the card its self. Also i would like to be able to put in the detail for the MUST HAVES so please Crete a box that i can alter depending on who in my business needs the cards. Thank you

Target Market(s)

Any one looking to build a house/ townhouse or duplex

Industry/Entity Type

Home Builder

Contact Information for Business Card

I would like the card to have the logo on the card and the must haves

Font styles to use
Sans Serif

Requirements
Must have
• Name
• Phone Number
• Email Address
• Website
• Licence Number
• Abn

```html
<!DOCTYPE html>
<html lang="en">
<head>
<meta charset="utf-8">
<title>Coastline Builders – Business Card</title>
<link href="https://fonts.googleapis.com/css2?family=Arimo:wght@400;700&display=swap" rel="stylesheet">
<style>
  :root {
    --gold: #c9a349;
    --gold-light: #dcbc68;
    --gold-dark: #b48d36;
    --ink: #111111;
    --grey: #6b6b6b;
    --paper: #ffffff;
    --backdrop: #ece9e4;
  }
  * { margin: 0; padding: 0; box-sizing: border-box; }
  html, body {
    width: 1200px; height: 950px; overflow: hidden;
    background: var(--backdrop);
    font-family: "Arimo", Arial, sans-serif;
  }
  .stage { position: relative; width: 1200px; height: 950px; }

  .card {
    position: absolute; width: 700px; height: 400px;
    box-shadow: 0 10px 30px rgba(0,0,0,.25);
    overflow: hidden;
  }

  /* Front card */
  .card-front {
    left: 110px; top: 45px;
    background: linear-gradient(135deg, var(--gold-light), var(--gold) 55%, var(--gold-dark));
  }
  .front-brand {
    position: absolute; left: 0; right: 0; top: 140px;
    display: flex; justify-content: center; align-items: center; gap: 14px;
  }
  .brand-mark { width: 26px; height: 26px; background: var(--ink); }
  .brand-name {
    font-weight: 700; font-size: 40px; color: var(--ink);
    letter-spacing: 1px; text-transform: uppercase;
  }
  .front-web {
    position: absolute; left: 0; right: 0; top: 262px;
    text-align: center; color: var(--paper);
    font-size: 17px; letter-spacing: 6px;
  }

  /* Back card */
  .card-back { left: 390px; top: 505px; background: var(--paper); }
  .back-brand {
    position: absolute; right: 34px; top: 46px;
    display: flex; align-items: center; gap: 10px;
  }
  .back-brand .brand-mark { width: 20px; height: 20px; }
  .back-brand .brand-name { font-size: 26px; }
  .brand-rule {
    position: absolute; left: 430px; right: 30px; top: 138px;
    height: 1.5px; background: var(--ink);
  }
  .abn {
    position: absolute; right: 36px; top: 176px;
    font-size: 15px; color: var(--grey);
  }
  .card-rule {
    position: absolute; left: 0; right: 40px; top: 232px;
    height: 1px; background: #333;
  }
  .card-bands { position: absolute; left: 0; top: 0; }
  .back-web {
    position: absolute; right: 24px; top: 306px;
    color: var(--paper); font-size: 15px; letter-spacing: 3px;
    white-space: nowrap;
  }
  .holder-name {
    position: absolute; left: 40px; top: 282px;
    color: var(--gold); font-size: 22px;
  }
  .holder-rule {
    position: absolute; left: 40px; top: 316px;
    width: 38px; height: 1.5px; background: var(--ink);
  }
  .contact {
    position: absolute; left: 40px;
    display: flex; align-items: center; gap: 10px;
    font-size: 17px; color: var(--grey);
  }
  .contact-phone { top: 326px; }
  .contact-email { top: 350px; }
  .contact svg { width: 16px; height: 16px; fill: var(--gold); }
</style>
</head>
<body>
<main class="stage">

  <section class="card card-front">
    <div class="front-brand">
      <span class="brand-mark"></span>
      <span class="brand-name">Coastline Builders</span>
    </div>
    <p class="front-web">www.coastlinebuild.com</p>
  </section>

  <section class="card card-back">
    <svg class="card-bands" width="700" height="400" viewBox="0 0 700 400" aria-hidden="true">
      <polygon points="0,380 380,380 368,400 0,400" fill="var(--gold)"/>
      <polygon points="396,286 700,286 700,400 348,400" fill="var(--ink)"/>
    </svg>

    <div class="back-brand">
      <span class="brand-mark"></span>
      <span class="brand-name">Coastline Builders</span>
    </div>
    <div class="brand-rule"></div>
    <p class="abn">Abn 7654321</p>
    <div class="card-rule"></div>

    <p class="back-web">www.coastlinebuild.com</p>

    <p class="holder-name">Sam Harlow</p>
    <div class="holder-rule"></div>
    <p class="contact contact-phone">
      <svg viewBox="0 0 24 24" aria-hidden="true"><path d="M6.6 10.8a15.1 15.1 0 0 0 6.6 6.6l2.2-2.2a1 1 0 0 1 1-.25 11.4 11.4 0 0 0 3.6.57 1 1 0 0 1 1 1V20a1 1 0 0 1-1 1A17 17 0 0 1 3 4a1 1 0 0 1 1-1h3.5a1 1 0 0 1 1 1c0 1.25.2 2.45.57 3.57a1 1 0 0 1-.25 1z"/></svg>
      555 0142 7788
    </p>
    <p class="contact contact-email">
      <svg viewBox="0 0 24 24" aria-hidden="true"><path d="M2 5h20v14H2z M2 5l10 8 10-8" fill="var(--gold)" stroke="#fff" stroke-width="1.5"/></svg>
      name@coastlinebuild.com
    </p>
  </section>

</main>
</body>
</html>
```